Stunning Podcast Cover Design for The Morning Harbor Hour!!

I need a design for my new podcast.
I will need it in a variety of size/formats, such as a large version for my podcast website homepage, the thumbnail for Tunewell, Pondcast, Vexa Stream and more.

The podcast is called "The Morning Harbor Hour" and it includes topics such as: business, entrepreneurship, finance, budgeting, estate planning, end-of-life planning, travel, business and personal stories featuring people from all over the world, life in general, and more.

I don't have a vision in mind so am looking for creativity but it definitely needs to have the colour gold in it somewhere! No cartoon characters please.

I will provide comments/feedback to each designer.

***UPDATE: Please see some photos of me that can be used in the podcast design.

Here is some tips on creating podcast designs. https://www.castleafy.example/blog/10-tips-create-awesome-podcast-artwork

Target Market(s)

Adults 25 - 65

Font styles to use
Other font styles liked:
• something modern - see my company logo as an example

Colors

Designer to choose colors to be used in the design.

Requirements
Must have
• The colour gold in it
Nice to have
• I feel like the word "The" should be smaller then the other three words.
• I would like to see designs with a white coloured background and a black coloured one also...
• Perhaps designs with a filter over the photo, and without.
• Perhaps use my photo, or don't use my photo!
• Please see some photos of me that can be used in the podcast design.
• Here is some tips on creating podcast designs. https://www.castleafy.example/blog/10-tips-create-awesome-podcast-artwork
Should not have
• cartoon characters
• Corny 1990's "Evenings Among the Gilded and Glamorous" look - see https://www.vidorama.example/watch?v=Q7T2KX8PLBZ

```html
<!DOCTYPE html>
<html lang="en">
<head>
<meta charset="utf-8">
<title>The Morning Harbor Hour — Podcast Cover</title>
<link rel="stylesheet" href="https://fonts.googleapis.com/css2?family=Archivo+Black&display=swap">
<style>
  :root {
    --bg-center: #243142;
    --bg-mid: #141a22;
    --bg-edge: #07090c;
    --title-white: #ffffff;
    --gold-top: #ffc80a;
    --gold-bottom: #f59d1c;
    --badge-ink: #0a0a0a;
    --city-haze: #1a2a38;
    --city-blue: #21394c;
    --city-teal: #2b4a5a;
    --city-lights: #6a5a3a;
    --city-deep: #0a121a;
  }
  * { margin: 0; padding: 0; box-sizing: border-box; }
  html, body {
    width: 1200px;
    height: 1200px;
    overflow: hidden;
    background: var(--bg-edge);
  }
  .cover {
    position: relative;
    width: 1200px;
    height: 1200px;
    overflow: hidden;
    background:
      radial-gradient(ellipse 60% 55% at 50% 42%, var(--bg-center) 0%, var(--bg-mid) 55%, var(--bg-edge) 100%);
    font-family: "Archivo Black", "Arial Black", sans-serif;
  }
  .cover__skyline {
    position: absolute;
    left: 0;
    right: 0;
    top: 795px;
    bottom: 0;
    background:
      radial-gradient(ellipse 45% 55% at 30% 70%, rgba(106, 90, 58, 0.55) 0%, transparent 70%),
      radial-gradient(ellipse 45% 55% at 75% 65%, rgba(106, 90, 58, 0.45) 0%, transparent 70%),
      linear-gradient(180deg, var(--city-haze) 0%, var(--city-blue) 30%, var(--city-teal) 60%, var(--city-deep) 100%);
  }
  .title {
    position: absolute;
    left: 0;
    right: 0;
    text-align: center;
    color: var(--title-white);
    line-height: 1;
    text-transform: uppercase;
  }
  .title__small {
    top: 96px;
    font-size: 72px;
    letter-spacing: 1px;
  }
  .title__line {
    font-size: 148px;
    letter-spacing: -2px;
  }
  .title__line--first { top: 186px; }
  .title__line--second { top: 362px; }
  .badge {
    position: absolute;
    left: 307px;
    top: 544px;
    width: 587px;
    height: 173px;
    border-radius: 24px;
    background: linear-gradient(180deg, var(--gold-top) 0%, var(--gold-bottom) 100%);
    display: flex;
    align-items: center;
    justify-content: center;
  }
  .badge__word {
    color: var(--badge-ink);
    font-size: 132px;
    line-height: 1;
    letter-spacing: 2px;
    text-transform: uppercase;
    text-shadow: 0 3px 4px rgba(0, 0, 0, 0.35);
  }
</style>
</head>
<body>
  <main class="cover">
    <div class="cover__skyline" role="img" aria-label="Photo of a night-time city skyline with lit office towers"></div>
    <h1>
      <span class="title title__small">The</span>
      <span class="title title__line title__line--first">Morning</span>
      <span class="title title__line title__line--second">Harbor</span>
      <span class="badge"><span class="badge__word">Hour</span></span>
    </h1>
  </main>
</body>
</html>
```